Boat business cards

I'm looking for business cards with the two logos I've attached. I don't have an specific idea in mind and open to anything. All the usual info will be on the card. Name, position in company, nr, email, address, ect. The company rents out these two boats for charters and fishing.

```html
<!DOCTYPE html>
<html lang="en">
<head>
<meta charset="UTF-8">
<title>Silver Tide Business Cards</title>
<link href="https://fonts.googleapis.com/css2?family=Poppins:wght@400;500;600&display=swap" rel="stylesheet">
<style>
  :root {
    --page-bg: #e9ebee;
    --card-bg: #ffffff;
    --ink: #1b1b1b;
    --sea-blue: #739fcb;
    --sea-blue-soft: #a9c3de;
    --hull-tan: #8c6a3f;
    --tan-soft: #b79a72;
    --wave-gray: #575757;
    --white: #ffffff;
  }
  * { margin: 0; padding: 0; box-sizing: border-box; }
  html, body { width: 1200px; height: 900px; overflow: hidden; }
  body {
    background: var(--page-bg);
    font-family: "Poppins", sans-serif;
    position: relative;
  }
  .card {
    position: absolute;
    left: 320px;
    width: 560px;
    height: 320px;
    background: var(--card-bg);
    border-radius: 22px;
    overflow: hidden;
    box-shadow: 0 6px 22px rgba(0,0,0,0.14);
  }
  .card--front { top: 110px; }
  .card--back { top: 470px; }

  /* Front */
  .front-mark {
    position: absolute;
    left: 50%;
    top: 62px;
    transform: translateX(-50%);
    display: flex;
    flex-direction: column;
    align-items: center;
  }
  .yacht-art {
    width: 250px;
    height: 110px;
    border-radius: 8px;
    background: linear-gradient(180deg, #eef0f2 0%, var(--tan-soft) 60%, var(--sea-blue-soft) 100%);
  }
  .brand-name {
    margin-top: 22px;
    font-size: 34px;
    font-weight: 500;
    color: var(--ink);
    letter-spacing: 1px;
  }

  /* Back */
  .waves { position: absolute; inset: 0; }
  .boat-art {
    position: absolute;
    left: 40px;
    top: 30px;
    width: 250px;
    height: 105px;
    border-radius: 8px;
    background: linear-gradient(160deg, #e6e9ec 0%, var(--sea-blue-soft) 55%, var(--sea-blue) 100%);
  }
  .boat-name {
    position: absolute;
    left: 40px;
    top: 142px;
    width: 250px;
    text-align: center;
    font-size: 24px;
    font-weight: 500;
    line-height: 1.3;
    color: var(--wave-gray);
  }
  .holder {
    position: absolute;
    right: 36px;
    top: 22px;
    text-align: right;
  }
  .holder-name { font-size: 22px; font-weight: 500; color: var(--ink); line-height: 1.1; }
  .holder-role { font-size: 14px; font-weight: 500; color: var(--hull-tan); letter-spacing: 0.5px; }
  .contact {
    position: absolute;
    right: 22px;
    top: 150px;
    list-style: none;
    color: var(--white);
    font-size: 12.5px;
    line-height: 1.45;
    text-align: right;
  }
  .contact li { display: flex; justify-content: flex-end; align-items: flex-start; gap: 8px; }
  .contact .icon { width: 13px; height: 13px; flex: none; margin-top: 2px; }
  .contact .icon-spacer { width: 13px; flex: none; }
</style>
</head>
<body>

<section class="card card--front">
  <div class="front-mark">
    <div class="yacht-art" role="img" aria-label="Illustration of the Silver Tide motor yacht on blue water lines"></div>
    <p class="brand-name">Silver Tide</p>
  </div>
</section>

<section class="card card--back">
  <svg class="waves" viewBox="0 0 560 320" preserveAspectRatio="none" aria-hidden="true">
    <path d="M0,264 C150,256 262,234 312,176 C362,114 452,82 560,78 L560,320 L0,320 Z" fill="var(--sea-blue)"/>
    <path d="M0,238 C150,238 250,222 302,176 C264,232 160,258 0,260 Z" fill="var(--wave-gray)"/>
    <path d="M110,302 C240,280 322,250 362,190 C402,128 462,96 540,86" fill="none" stroke="var(--white)" stroke-width="5" stroke-linecap="round"/>
  </svg>

  <div class="boat-art" role="img" aria-label="Illustration of the Blue Current sport fishing boat"></div>
  <p class="boat-name">Blue Current</p>

  <div class="holder">
    <p class="holder-name">Daniel Reyes</p>
    <p class="holder-role">Managing Director</p>
  </div>

  <ul class="contact">
    <li>555-214-0187
      <svg class="icon" viewBox="0 0 24 24"><path d="M6.6 10.8a15 15 0 0 0 6.6 6.6l2.2-2.2a1 1 0 0 1 1-.25 11.4 11.4 0 0 0 3.6.57 1 1 0 0 1 1 1V20a1 1 0 0 1-1 1A17 17 0 0 1 3 4a1 1 0 0 1 1-1h3.5a1 1 0 0 1 1 1c0 1.25.2 2.45.57 3.6a1 1 0 0 1-.25 1z" fill="#fff"/></svg>
    </li>
    <li>daniel@silvertide.com
      <svg class="icon" viewBox="0 0 24 24"><rect x="2" y="5" width="20" height="14" rx="1.5" fill="#fff"/><path d="M3 6l9 7 9-7" fill="none" stroke="var(--sea-blue)" stroke-width="2"/></svg>
    </li>
    <li>88 Harbor Street, Suite 12,
      <svg class="icon" viewBox="0 0 24 24"><path d="M12 2a7 7 0 0 0-7 7c0 5 7 13 7 13s7-8 7-13a7 7 0 0 0-7-7z" fill="#fff"/><circle cx="12" cy="9" r="2.6" fill="var(--sea-blue)"/></svg>
    </li>
    <li>Lakeport, MI 49000<span class="icon-spacer"></span></li>
  </ul>
</section>

</body>
</html>
```